Polystyrene Environmental Synopsis

We need a fact sheet for quick reference that groups information units and has a simple but engaging visual presentation of the text and various infographics. We are a trade association representing polystyrene foam manufacturers and this piece is intended to help our members provide effective messaging to their sales personnel.

To view our typical company design/style please see our website at www.foamtradeunion.org. Our primary RGB colors are: (187,140,9); (94,47,29); (94,138,164); and (164,167,15). Secondary RGB colors are (249,162,28) and (218,210,208). Our title/header font is DIN Next LT Pro and our copy font is Calibri 10.5 pt. We can deviate from the font specification if beneficial.

Target Market(s)

Polystyrene manufacturer plant workers and other employees.

Font styles to use
Sans Serif

Requirements
Must have
• Information presentation must be clean and easy to reference.

```html
<!DOCTYPE html>
<html lang="en">
<head>
<meta charset="utf-8">
<title>EPS Talking Points</title>
<link rel="stylesheet" href="https://fonts.googleapis.com/css2?family=Saira+Condensed:wght@600;700&family=Carlito:wght@400;700&display=swap">
<style>
:root{
  --gold:#BB8C09;
  --gold-light:#C99A12;
  --brown:#5E2F1D;
  --blue:#5E8AA4;
  --olive:#A4A70F;
  --olive-light:#B3B61E;
  --orange:#F9A21C;
  --warm-gray:#DAD2D0;
  --panel:#F0F0F0;
  --page:#F4F4F4;
  --ink:#2E2E2E;
  --white:#FFFFFF;
}
*{box-sizing:border-box;margin:0;padding:0}
html,body{width:740px;height:1200px;overflow:hidden;background:var(--white)}
.canvas{position:relative;width:740px;height:1200px;overflow:hidden;background:var(--page);font-family:"Carlito",Calibri,sans-serif;color:var(--ink)}

/* header */
.header{position:absolute;left:0;top:0;width:740px;height:90px;background:var(--white);z-index:2}
.title{position:absolute;left:20px;top:-4px;font-family:"Saira Condensed","Arial Narrow",sans-serif;font-weight:700;font-size:58px;letter-spacing:8px;color:var(--gold);line-height:1.1}
.intro{position:absolute;left:22px;top:63px;width:610px;font-size:9.6px;line-height:1.3;color:var(--ink)}
.brand{position:absolute;left:640px;top:4px;width:96px;text-align:center}
.brand-dot{display:block;width:46px;height:46px;margin:0 auto 3px;border-radius:50%;background:var(--gold)}
.brand-name{display:block;font-family:"Carlito",Calibri,sans-serif;font-size:12.5px;line-height:1;color:var(--gold)}

/* defense line */
.defense{position:absolute;left:0;top:92px;width:740px;height:158px;background:var(--panel);padding:5px 22px 0 20px}
.defense h2{font-family:"Saira Condensed","Arial Narrow",sans-serif;font-weight:700;font-size:28px;letter-spacing:2.5px;color:var(--blue);line-height:1.1;margin-bottom:3px}
.defense p{font-size:9.3px;line-height:1.36;text-align:justify}
.defense .gap{margin-top:9px}
.defense b{font-family:"Saira Condensed","Arial Narrow",sans-serif;font-weight:700;letter-spacing:.5px;font-size:10px}

/* section bands */
.band{position:absolute;left:0;width:740px;background:var(--olive);display:flex;align-items:center;justify-content:center;gap:18px}
.band h3{font-family:"Saira Condensed","Arial Narrow",sans-serif;font-weight:700;color:var(--white);font-size:38px;letter-spacing:5px;line-height:1}
.band-icon{width:46px;height:46px;flex:none}
.divider{position:absolute;left:0;width:740px;height:12px;background:var(--brown)}

/* cards */
.card{position:absolute}
.card svg.shape{position:absolute;left:0;top:0}
.card-title{position:absolute;left:0;text-align:center;font-family:"Saira Condensed","Arial Narrow",sans-serif;font-weight:700;color:var(--white);letter-spacing:1px;line-height:1.05}
.card-text{position:absolute;font-size:8.4px;line-height:1.28;text-align:justify}
.card-text .ind{padding-left:8px}

.bin .card-title{width:190px;top:8px;font-size:16px}
.bin .card-text{color:var(--white)}

.cup .card-title{width:200px;top:3px;font-size:12.5px;letter-spacing:1.4px}
.cup .card-text{color:var(--ink)}

.clip .card-title{width:100%;font-size:17px;letter-spacing:1.2px}
.clip .card-text{color:var(--ink);font-size:8.2px}
</style>
</head>
<body>
<div class="canvas">

  <header class="header">
    <h1 class="title">EPS TALKING POINTS</h1>
    <p class="intro">Polystyrene bans, recycling, and human health are top objections facing the EPS industry. When confronted with false allegations about EPS, here are some fast facts to help respond proactively. Perfect for packaging conferences, social media, and sales objectives.</p>
    <div class="brand"><span class="brand-dot"></span><span class="brand-name">Foam Trade<br>Union</span></div>
  </header>

  <section class="defense">
    <h2>Polystyrene Defense Line</h2>
    <p><b>Making Your Point</b> - Speaking with confidence means knowing your material. When responding to misstatements be prepared to challenge the source with factual information. Using a question format is less confrontational, e.g., “Did you know...” or “Were you aware...”? Make affirmative statements whenever possible; avoid restating the misinformation in your response. When addressing someone that refuses to give reasonable consideration to new information, we recommend responding, “It’s unfortunate you’re not willing to look into this further.”</p>
    <p>When given the opportunity to address an individual or an audience about EPS sustainability, focus on three (3) specific talking points to keep the discussion or presentation focused. Plan your talking points and don’t deviate; this is an effective strategy for dealing with media inquiries as well.</p>
    <p class="gap"><b>Have a Bigger Voice</b> - The more educated we are, the more educated others will be. Share this document with your employees even if they do not deal directly with your customers or specific packaging audiences. Everyone working within the EPS industry should be aware of the strong environmental profile for EPS.</p>
  </section>

  <!-- RECYCLING -->
  <div class="band" style="top:252px;height:58px">
    <h3>RECYCLING</h3>
    <svg class="band-icon" viewBox="0 0 46 46" aria-hidden="true">
      <circle cx="23" cy="23" r="23" fill="var(--brown)"/>
      <g fill="none" stroke="var(--olive-light)" stroke-width="4" stroke-linecap="round">
        <path d="M17 15 L23 11 L29 20"/>
        <path d="M33 26 L31 33 L21 33"/>
        <path d="M15 33 L11 27 L16 18"/>
      </g>
      <g fill="var(--olive-light)">
        <path d="M26 20 L32 22 L33 15 Z"/>
        <path d="M22 29 L18 33 L23 37 Z"/>
        <path d="M13 19 L19 17 L16 12 Z"/>
      </g>
    </svg>
  </div>

  <div class="card bin" style="left:60px;top:314px;width:190px;height:264px">
    <svg class="shape" width="190" height="264" viewBox="0 0 190 264" aria-hidden="true">
      <path d="M6 4 Q6 0 10 0 H180 Q184 0 184 4 V36 H6 Z" fill="#9EA10C"/>
      <path d="M16 36 H174 L166 232 H24 Z" fill="var(--olive-light)"/>
      <rect x="22" y="36" width="146" height="4" fill="#8F920A"/>
      <rect x="24" y="224" width="12" height="36" rx="3" fill="#111"/>
      <rect x="154" y="224" width="12" height="36" rx="3" fill="#111"/>
    </svg>
    <div class="card-title">EPS is Recyclable</div>
    <div class="card-text" style="left:24px;top:47px;width:142px">
      <p>• Historically, EPS recycling averages ~18% over a 25-year trendline.</p>
      <p>• EPS recycling is most successful in commercial waste streams with large volume sources of EPS waste.</p>
      <p>• Consumer access to EPS recycling sometimes requires extra effort, but with proper equipment &amp; handling, it is successful in many communities.</p>
      <p>• Creative problem solving for challenging recycling scenarios means Harborline Market, NutriWay Foods, Kettle &amp; Vine, Brightwave Appliances, Circuit Depot, Prairie Cut Meats are committed to long term EPS recycling.</p>
    </div>
  </div>

  <div class="card bin" style="left:274px;top:314px;width:190px;height:264px">
    <svg class="shape" width="190" height="264" viewBox="0 0 190 264" aria-hidden="true">
      <path d="M2 4 Q2 0 6 0 H184 Q188 0 188 4 V36 H2 Z" fill="#55809A"/>
      <path d="M14 36 H176 L166 232 H24 Z" fill="var(--blue)"/>
      <rect x="20" y="36" width="150" height="4" fill="#4B7088"/>
      <rect x="24" y="224" width="12" height="36" rx="3" fill="#111"/>
      <rect x="154" y="224" width="12" height="36" rx="3" fill="#111"/>
    </svg>
    <div class="card-title" style="font-size:14.5px;top:2px">New EPS Recycling<br>Technologies Are Emerging</div>
    <div class="card-text" style="left:22px;top:110px;width:146px">
      <p>• Pyrolysis - a chemical reprocessing method - increases the ability to recycle contaminated EPS waste.</p>
      <p>• Two new facilities opened in 2018.</p>
    </div>
  </div>

  <div class="card bin" style="left:488px;top:314px;width:190px;height:264px">
    <svg class="shape" width="190" height="264" viewBox="0 0 190 264" aria-hidden="true">
      <path d="M2 4 Q2 0 6 0 H184 Q188 0 188 4 V36 H2 Z" fill="var(--gold)"/>
      <path d="M14 36 H176 L166 232 H24 Z" fill="var(--gold-light)"/>
      <rect x="20" y="36" width="150" height="4" fill="#A67C08"/>
      <rect x="24" y="224" width="12" height="36" rx="3" fill="#111"/>
      <rect x="154" y="224" width="12" height="36" rx="3" fill="#111"/>
    </svg>
    <div class="card-title" style="font-size:14.5px;top:2px">EPS End-Markets Show<br>Consistent Growth</div>
    <div class="card-text" style="left:20px;top:78px;width:148px">
      <p>• It is used as recycled content in new EPS packaging and other EPS products.</p>
      <p>• Markets for recycled content EPS include:</p>
      <p class="ind">◦ Crown Molding</p>
      <p class="ind">◦ Surfboards</p>
      <p class="ind">◦ Picture Frames</p>
      <p class="ind">◦ Other Rigid Polystyrene</p>
      <p>Applications</p>
    </div>
  </div>

  <div class="divider" style="top:578px"></div>

  <!-- EPS BANS -->
  <div class="band" style="top:592px;height:58px">
    <h3>EPS BANS</h3>
    <svg class="band-icon" viewBox="0 0 46 46" aria-hidden="true">
      <circle cx="23" cy="23" r="23" fill="var(--brown)"/>
      <path d="M16 14 H30 L28 34 H18 Z" fill="var(--white)"/>
      <circle cx="23" cy="24" r="12" fill="none" stroke="#D0202A" stroke-width="3.5"/>
      <line x1="14.5" y1="15.5" x2="31.5" y2="32.5" stroke="#D0202A" stroke-width="3.5"/>
    </svg>
  </div>

  <div class="card cup" style="left:44px;top:658px;width:200px;height:224px">
    <svg class="shape" width="200" height="224" viewBox="0 0 200 224" aria-hidden="true">
      <defs>
        <linearGradient id="cupShade" x1="0" x2="1">
          <stop offset="0" stop-color="#E4E4E4"/><stop offset=".12" stop-color="#FFFFFF"/>
          <stop offset=".88" stop-color="#FFFFFF"/><stop offset="1" stop-color="#E4E4E4"/>
        </linearGradient>
      </defs>
      <path d="M12 0 H188 L200 34 H0 Z" fill="var(--olive)"/>
      <path d="M10 36 H190 L176 222 H24 Z" fill="url(#cupShade)"/>
    </svg>
    <div class="card-title">Material Substitutions<br>Are Risky</div>
    <div class="card-text" style="left:14px;top:52px;width:172px">
      <p>• Recent studies show that heavier alternatives to lightweight plastics can significantly increase raw material requirements, energy consumption &amp; landfill volume.</p>
      <p>• On a global scale, environmental costing indicates that plastics alternatives may cost $400 to $500 billion more (4 to 5 times more).</p>
      <p>• Meat, fish &amp; produce shipped in EPS have a longer shelf life, leading to less food waste.</p>
    </div>
  </div>

  <div class="card cup" style="left:270px;top:658px;width:200px;height:224px">
    <svg class="shape" width="200" height="224" viewBox="0 0 200 224" aria-hidden="true">
      <path d="M12 0 H188 L200 34 H0 Z" fill="var(--blue)"/>
      <path d="M10 36 H190 L176 222 H24 Z" fill="url(#cupShade)"/>
    </svg>
    <div class="card-title">EPS Is More Sustainable<br>Than Most People Imagine</div>
    <div class="card-text" style="left:22px;top:80px;width:156px">
      <p>• EPS foam is of 98% air, which results in lower energy consumption.</p>
      <p>• Life cycle analyses show that EPS has far less impact on the environment than other competitive materials for the same use; in particular paper.</p>
    </div>
  </div>

  <div class="card cup" style="left:494px;top:658px;width:200px;height:224px">
    <svg class="shape" width="200" height="224" viewBox="0 0 200 224" aria-hidden="true">
      <path d="M12 0 H188 L200 34 H0 Z" fill="var(--gold)"/>
      <path d="M10 36 H190 L176 222 H24 Z" fill="url(#cupShade)"/>
    </svg>
    <div class="card-title">Litter Problems Are Not<br>Material Dependent</div>
    <div class="card-text" style="left:18px;top:80px;width:160px">
      <p>• A litter audit in San Francisco confirmed that a food service ban on polystyrene foam only changed the type of litter but did not reduce it.</p>
      <p>• Improper disposal of any material contributes to litter, whether it is EPS or another material.</p>
    </div>
  </div>

  <div class="divider" style="top:888px"></div>

  <!-- HUMAN HEALTH & SAFETY -->
  <div class="band" style="top:900px;height:66px">
    <h3>HUMAN HEALTH &amp; SAFETY</h3>
    <svg class="band-icon" viewBox="0 0 46 46" aria-hidden="true">
      <circle cx="23" cy="23" r="23" fill="var(--brown)"/>
      <path d="M23 9 L34 13 V23 Q34 32 23 37 Q12 32 12 23 V13 Z" fill="var(--white)"/>
      <path d="M21 16 H25 V21 H30 V25 H25 V30 H21 V25 H16 V21 H21 Z" fill="#D0202A"/>
    </svg>
  </div>

  <div class="card clip" style="left:46px;top:970px;width:176px;height:214px">
    <svg class="shape" width="176" height="214" viewBox="0 0 176 214" aria-hidden="true">
      <rect x="2" y="20" width="172" height="192" rx="7" fill="var(--white)" stroke="var(--olive)" stroke-width="4"/>
      <rect x="54" y="10" width="68" height="14" rx="3" fill="var(--gold)"/>
      <circle cx="88" cy="10" r="6" fill="none" stroke="var(--gold)" stroke-width="3"/>
    </svg>
    <div class="card-title" style="top:38px;color:var(--gold);font-size:16px;line-height:.95">There Is Very Little<br>Residual Styrene<br>in EPS</div>
    <div class="card-text" style="left:12px;top:90px;width:152px">
      <p>• The amount of styrene that might exist in finished polystyrene is extremely small - often lower than naturally occurring styrene found in everyday food items like coffee, strawberries, and cinnamon.</p>
      <p>• All chemicals need to be assessed in terms of risk versus exposure. Risks can be zero, negligible or harmful.</p>
    </div>
  </div>

  <div class="card clip" style="left:280px;top:970px;width:176px;height:214px">
    <svg class="shape" width="176" height="214" viewBox="0 0 176 214" aria-hidden="true">
      <rect x="2" y="20" width="172" height="192" rx="7" fill="var(--white)" stroke="var(--blue)" stroke-width="4"/>
      <rect x="54" y="10" width="68" height="14" rx="3" fill="var(--gold)"/>
      <circle cx="88" cy="10" r="6" fill="none" stroke="var(--gold)" stroke-width="3"/>
    </svg>
    <div class="card-title" style="top:40px;color:var(--blue);font-size:16.5px;line-height:.95">EPS Is An Organic<br>Polymer</div>
    <div class="card-text" style="left:12px;top:90px;width:152px">
      <p>• Polystyrene is an organic compound consisting of hydrogen and carbon.</p>
      <p>• Polystyrene is chemically very inert, being resistant to acids and bases but is easily dissolved by many chlorinated solvents, and many aromatic hydrocarbon solvents.</p>
    </div>
  </div>

  <div class="card clip" style="left:516px;top:970px;width:176px;height:214px">
    <svg class="shape" width="176" height="214" viewBox="0 0 176 214" aria-hidden="true">
      <rect x="2" y="20" width="172" height="192" rx="7" fill="var(--white)" stroke="var(--gold)" stroke-width="4"/>
      <rect x="54" y="10" width="68" height="14" rx="3" fill="var(--gold)"/>
      <circle cx="88" cy="10" r="6" fill="none" stroke="var(--gold)" stroke-width="3"/>
    </svg>
    <div class="card-title" style="top:50px;color:var(--gold);font-size:17px">EPS Is Safe</div>
    <div class="card-text" style="left:12px;top:90px;width:152px">
      <p>• Polystyrene foam is approved for food contact by the Food Safety Board and other global regulatory agencies.</p>
      <p>• According to the National Marine Research Office (NMRO), although marine debris is a global issue, there are significant gaps in our understanding of the problem.</p>
    </div>
  </div>

</div>
</body>
</html>
```